A SEASON OF EMBERS book cover needed

Hello friends! I'm working toward self-publishing my first novel in the next few months, and I'm looking to have a professional-looking, 6 in x 9 in cover to go along with the ebook release. I’m not looking for much, but the key is that it must look professional. I don’t want decorative fonts, but I also don’t want it to just look like Helvetica or Times New Roman.The text for the cover should be:A TIME FOR GREATNESSKARLIS WILDEI have attached a few images to show you where my head is at. I created a book cover myself on paint that looks horribly amateur, but it draws inspiration from a HPB campaign poster(also attached) where the title of the novel comes from. If you can make that same kind of cover, but make it look professional, that would be amazing! If you have other, simple ideas, I am also very, very open.Attached as well are a couple of simple, recent book covers that I like. That is the kind of thing that I am looking for.If this goes well, I may do a paperback release. In that case, I may need to contact you again for an additional fee to create the rest of the wraparound design. In addition, the book is the first in a projected trilogy, so there may be opportunities for you in the future for sequel covers.About the book: A SEASON OF EMBERS is a gripping, standalone thriller with an exciting take on history, relationships, conspiracy theories, and the current, volatile political state of America. In the present day, new information surrounding the 1963 assassination of Harold P. Brisbane comes to light and Milo Fenwright, a young, best-selling journalist still reconciling his success with his dark past, finds himself more personally connected than he ever could have expected. But the story becomes something even bigger when an assassination attempt on the current demagogic president sends the whole world of journalism into a scramble, and Milo finds himself confronted by an extremely difficult question: Is democracy real, or has it been an illusion fostered by these secretive ‘Stewards of the Union’ since 1776? Travelling across Syria, Canada, and the United States of America, the story becomes more unbelievable—and more personal—as increasingly prominent figures begin to enter Milo’s orbit, intent on keeping their secrets safe by whatever means necessary.

Colors

Designer to choose colors to be used in the design.

Requirements
Must have
• Text
• Simplicity
• Professional look
Should not have
• Cheap fonts
• Complicated images

```html
<!DOCTYPE html>
<html lang="en">
<head>
<meta charset="utf-8">
<title>A Season of Embers — Tomas Reyvik</title>
<link rel="stylesheet" href="https://fonts.googleapis.com/css2?family=Bebas+Neue&family=Courier+Prime:wght@700&display=swap">
<style>
  :root {
    --paper: #f2f0ec;
    --paper-shade: #dcd6cd;
    --navy: #2c3a7c;
    --red: #c9262d;
  }
  * { margin: 0; padding: 0; box-sizing: border-box; }
  html, body { width: 751px; height: 1200px; overflow: hidden; }
  body { background: var(--paper); }

  .cover {
    position: relative;
    width: 751px;
    height: 1200px;
    overflow: hidden;
    background:
      radial-gradient(ellipse 180px 90px at 700px 440px, rgba(180,170,155,0.35), transparent 70%),
      radial-gradient(ellipse 160px 120px at 60px 1000px, rgba(190,180,165,0.35), transparent 70%),
      radial-gradient(ellipse 220px 140px at 650px 1130px, rgba(200,190,175,0.3), transparent 70%),
      radial-gradient(ellipse 420px 500px at 50% 55%, #f7f6f3, var(--paper) 80%);
  }

  .flag-sweep {
    position: absolute;
    top: 0;
    left: 0;
    width: 751px;
    height: 400px;
  }

  .title {
    position: absolute;
    top: 452px;
    left: 0;
    width: 751px;
    font-family: "Bebas Neue", "Oswald", sans-serif;
    text-transform: uppercase;
  }
  .title-row {
    display: flex;
    justify-content: center;
    align-items: flex-start;
    gap: 14px;
    line-height: 0.78;
  }
  .title-row--first { color: var(--navy); }
  .title-row--second { color: var(--red); margin-top: 20px; }
  .title-small { font-size: 92px; padding-top: 4px; }
  .title-large--first { font-size: 236px; letter-spacing: 2px; }
  .title-small--second { font-size: 84px; padding-top: 4px; }
  .title-large--second { font-size: 178px; letter-spacing: 2px; }

  .star-row {
    position: absolute;
    top: 828px;
    left: 100px;
    width: 551px;
    height: 32px;
  }

  .subtitle {
    position: absolute;
    top: 900px;
    left: 0;
    width: 751px;
    text-align: center;
    font-family: "Courier Prime", "Courier New", monospace;
    font-weight: 700;
    font-size: 22px;
    letter-spacing: 15px;
    padding-left: 15px;
    color: var(--navy);
  }

  .author {
    position: absolute;
    top: 950px;
    left: 0;
    width: 751px;
    text-align: center;
    font-family: "Courier Prime", "Courier New", monospace;
    font-weight: 700;
    color: var(--navy);
    font-size: 96px;
    line-height: 112px;
    letter-spacing: 18px;
    padding-left: 18px;
  }
  .author-line { display: block; }
</style>
</head>
<body>
  <main class="cover">
    <svg class="flag-sweep" viewBox="0 0 751 400" role="img" aria-label="Painted brushstroke American flag sweeping across the top of the cover">
      <defs>
        <linearGradient id="sweepTone" x1="0" y1="0" x2="1" y2="0.4">
          <stop offset="0" stop-color="#2c3a7c"/>
          <stop offset="0.42" stop-color="#6a3b6a"/>
          <stop offset="0.6" stop-color="#c9262d"/>
          <stop offset="1" stop-color="#d6343a"/>
        </linearGradient>
      </defs>
      <path d="M0 0 H751 V60 C640 75 520 110 470 150 C560 150 650 170 720 200 C700 230 560 240 430 250 C320 275 200 310 80 385 C60 340 40 300 0 300 Z" fill="url(#sweepTone)"/>
    </svg>

    <h1 class="title">
      <span class="title-row title-row--first">
        <span class="title-small">A</span>
        <span class="title-large--first">Season</span>
      </span>
      <span class="title-row title-row--second">
        <span class="title-small--second">Of</span>
        <span class="title-large--second">Embers</span>
      </span>
    </h1>

    <svg class="star-row" viewBox="0 0 551 32" aria-hidden="true">
      <defs>
        <polygon id="star" points="16,1 19.8,11.4 31,11.6 22.1,18.4 25.3,29.2 16,22.8 6.7,29.2 9.9,18.4 1,11.6 12.2,11.4" fill="#2c3a7c"/>
      </defs>
      <use href="#star" x="0"/>
      <use href="#star" x="57.7"/>
      <use href="#star" x="115.4"/>
      <use href="#star" x="173.1"/>
      <use href="#star" x="230.8"/>
      <use href="#star" x="288.5"/>
      <use href="#star" x="346.2"/>
      <use href="#star" x="403.9"/>
      <use href="#star" x="461.6"/>
      <use href="#star" x="519"/>
    </svg>

    <p class="subtitle">A NOVEL</p>

    <p class="author">
      <span class="author-line">TOMAS</span>
      <span class="author-line">REYVIK</span>
    </p>
  </main>
</body>
</html>
```